Wound Care Flyer

Looking for a Trifold brochure that is modern and has a high aesthetic. (Specialty services) Would like the colors to center around Black and Gold. Possibly updating the logo. Attached is the old brochure and a document about our services.

```html
<!DOCTYPE html>
<html lang="en">
<head>
<meta charset="utf-8">
<title>Cedarbrook Wounds – Trifold Brochure</title>
<link href="https://fonts.googleapis.com/css2?family=Montserrat:wght@400;500;600;700;800&display=swap" rel="stylesheet">
<style>
  :root{
    --bg:#ececec;
    --black:#121212;
    --charcoal:#1d1d1d;
    --band:#262626;
    --gold:#d4b26a;
    --gold-light:#f4e8ad;
    --gold-mid:#cdb47c;
    --gold-deep:#a88a58;
    --ink:#151515;
    --text-light:#ededed;
    --photo-a:#e7e4df;
    --photo-b:#b9a6a6;
  }
  *{box-sizing:border-box;margin:0;padding:0}
  html,body{width:674px;height:1200px;overflow:hidden;background:var(--bg)}
  body{font-family:"Montserrat",sans-serif;color:var(--text-light);position:relative}
  .spread{position:absolute;left:20px;width:634px;height:490px;display:flex;box-shadow:0 10px 24px rgba(0,0,0,.18)}
  .spread--outside{top:70px}
  .spread--inside{top:620px}
  .panel{width:211.33px;height:100%;position:relative;padding:26px 18px;overflow:hidden}
  .panel--black{background:var(--black)}
  .panel--charcoal{background:var(--charcoal)}
  .panel--gold{background:linear-gradient(180deg,var(--gold-light) 0%,var(--gold-mid) 55%,var(--gold-deep) 100%);color:var(--ink)}
  .heading{font-weight:800;text-transform:uppercase;color:var(--gold);font-size:12px;line-height:1.1;letter-spacing:.2px}
  .panel--gold .heading{color:var(--ink)}
  .rule{width:26px;height:1.5px;background:var(--gold);margin:6px 0 10px}
  .panel--gold .rule{background:var(--ink)}
  .body-text{font-size:6.6px;line-height:1.45}
  .body-text + .body-text{margin-top:6px}
  .body-text strong{font-weight:700}
  .brand{display:flex;align-items:center;justify-content:center;gap:7px}
  .brand__dot{width:16px;height:16px;border:1.5px solid currentColor;border-radius:50%}
  .brand__name{font-weight:500;font-size:11px;letter-spacing:2px;text-transform:uppercase;line-height:1.3;text-align:center}
  .panel--black .brand{color:var(--gold)}
  .panel--gold .brand{color:var(--ink)}
  .service-list{list-style:none;margin-top:8px}
  .service-list li{display:flex;align-items:center;gap:7px;font-size:6.8px;margin-bottom:6px}
  .service-list li::before{content:"";width:9px;height:9px;border:1px solid var(--gold);border-radius:50%;flex:none}
  .contact{text-align:center;margin-top:48px}
  .contact .rule{margin:6px auto 10px}
  .contact__line{width:120px;height:1px;background:var(--ink);margin:16px auto}
  .icon-badge{width:20px;height:20px;border-radius:50%;background:var(--ink);display:flex;align-items:center;justify-content:center;margin:0 auto 8px}
  .phone{font-size:12px;font-weight:500;line-height:1.4}
  .email{font-size:8px;font-weight:500}
  .portrait{margin:22px auto 0;width:160px;height:250px;border-radius:8px;background:linear-gradient(160deg,var(--photo-a) 0%,#f3f1ee 45%,var(--photo-b) 100%)}
  .signature{margin-top:18px;text-align:center;font-weight:800;font-size:12px;color:var(--gold)}
  .subhead{margin-top:18px}
  .treatment-box{border:1px solid var(--ink);border-radius:3px;padding:7px 8px;margin-top:8px}
  .treatment-box h4{font-size:6.8px;font-weight:700;text-transform:uppercase;margin-bottom:4px}
  .treatment-box ul{padding-left:10px;font-size:6px;line-height:1.5}
  .treatment-box p{font-size:6px;line-height:1.4;margin-bottom:2px}
  .partner-item{display:flex;gap:10px;align-items:center;padding:11px 16px;margin:0 -18px}
  .partner-item:nth-child(odd){background:var(--band)}
  .partner-item__icon{width:18px;height:18px;border:1px solid var(--gold);border-radius:50%;flex:none}
  .partner-item h4{font-size:6.8px;font-weight:700;text-transform:uppercase;margin-bottom:3px}
  .partner-item p{font-size:5.8px;line-height:1.4;color:#cfcfcf}
  .care-photos{position:absolute;left:211.33px;bottom:0;width:422.67px;height:95px;display:flex}
  .care-photos div{flex:1}
  .care-photos .photo-1{background:linear-gradient(135deg,#e9e4dd,#a97b5c)}
  .care-photos .photo-2{background:linear-gradient(135deg,#f1ece7,#2d4fa8)}
  .care-photos .photo-3{background:linear-gradient(135deg,#f4f2ef,#c89a7c)}
</style>
</head>
<body>

<section class="spread spread--outside" aria-label="Brochure outside">
  <article class="panel panel--black">
    <h2 class="heading">About Us</h2>
    <div class="rule"></div>
    <p class="body-text">We provide an additional layer of expertise by utilizing advanced technology of biological skin substitute grafts. We pride ourselves in working in close coordination with the patient's care team, including home health services and <strong>THE PRIMARY CARE PHYSICIAN (PCP)</strong>. We ensure seamless integration without duplicating services, prioritizing collaborative care, sharing detailed notes and working closely with the patient's home health team on days between visits.</p>
    <p class="body-text">Serving the greater Northlake area (Ashford, Brookvale, Elm Ridge, Pinecrest, Harlow, Kessler, Marlow, Oakhurst)</p>
    <h2 class="heading subhead">Advanced<br>Wound Care</h2>
    <div class="rule"></div>
    <p class="body-text"><strong>Specializing in Biologic Skin Substitutes to treat:</strong></p>
    <ul class="service-list">
      <li>Pressure Injuries, Surgical/Trauma Wounds</li>
      <li>Venous/Arterial Wounds, Diabetic Wounds</li>
      <li>Diagnostic Testing</li>
      <li>Debridements</li>
      <li>Multidisciplinary Collaboration</li>
    </ul>
  </article>

  <article class="panel panel--gold">
    <div class="brand" style="margin-top:30px"><span class="brand__dot"></span><span class="brand__name">Cedarbrook<br>Wounds</span></div>
    <div class="contact">
      <h2 class="heading" style="font-size:14px">Contact</h2>
      <div class="rule"></div>
      <p class="body-text">Book your appointment today and take<br>the first step towards better health!</p>
      <div class="contact__line"></div>
      <div class="icon-badge">
        <svg width="10" height="10" viewBox="0 0 24 24"><path fill="#d4b26a" d="M6.6 10.8a15 15 0 0 0 6.6 6.6l2.2-2.2c.3-.3.7-.4 1-.2 1.1.4 2.3.6 3.6.6.6 0 1 .4 1 1V20c0 .6-.4 1-1 1A17 17 0 0 1 3 4c0-.6.4-1 1-1h3.5c.6 0 1 .4 1 1 0 1.2.2 2.4.6 3.6.1.3 0 .7-.2 1z"/></svg>
      </div>
      <p class="phone">(555) 014-2287<br>(555) 018-3346</p>
      <div class="contact__line"></div>
      <div class="icon-badge">
        <svg width="10" height="10" viewBox="0 0 24 24"><rect x="2" y="5" width="20" height="14" rx="2" fill="none" stroke="#d4b26a" stroke-width="2"/><path d="M2 6l10 7 10-7" fill="none" stroke="#d4b26a" stroke-width="2"/></svg>
      </div>
      <p class="email">cedarbrookwounds@example.com</p>
    </div>
  </article>

  <article class="panel panel--black">
    <div class="brand" style="margin-top:10px"><span class="brand__dot"></span><span class="brand__name">Cedarbrook<br>Wounds</span></div>
    <div class="portrait" role="img" aria-label="Portrait of the nurse practitioner in a white coat in a bright clinic"></div>
    <p class="signature">Maya Collins, FNP-C</p>
  </article>
</section>

<section class="spread spread--inside" aria-label="Brochure inside">
  <article class="panel panel--black">
    <h2 class="heading">Mobile<br>Wound Care</h2>
    <div class="rule"></div>
    <p class="body-text">With a focus on convenience, expertise, and compassion, we bring the highest standard of wound care directly to the patient's home. Working side-by-side with the patient's physician, our team of experienced specialists utilize cutting-edge technology and personalized treatment plans to ensure optimal healing and comfort. From thorough wound assessments to advanced therapies and ongoing support, we prioritize the wellbeing of our patients every step of the way. Whether it's managing chronic wounds, postsurgery recovery, we go above and beyond to provide comprehensive and compassionate care. With our concierge approach, we aim to make the healing journey as seamless and comfortable as possible, empowering our patients to live their best lives.</p>
    <h2 class="heading subhead">Personalized<br>Care Plan</h2>
    <div class="rule"></div>
    <p class="body-text">Customized care plans designed to meet the specific needs of each patient, ensuring optimal healing. Coordination and direction of care for other caregivers and clinicians, including home health.</p>
    <p class="body-text">Patient and Caregiver Education Providing education and support to patients and their caregivers to enhance understanding and promote self-care.</p>
  </article>

  <article class="panel panel--gold">
    <h2 class="heading">Leaders in Mobile Advanced Wound Care.</h2>
    <div class="rule"></div>
    <p class="body-text">We provide a complete wound management program for our patients that includes the use of advanced treatments, the creation of care plans, and coordination of care with other clinicians.</p>
    <p class="body-text">Our comprehensive in-home wound care services include:</p>
    <div class="treatment-box">
      <h4>Advanced Wound Assessment</h4>
      <ul><li>Thorough evaluation of wound type, size, and stage to develop a tailored treatment plan.</li></ul>
    </div>
    <div class="treatment-box">
      <h4>Cutting-Edge Treatments</h4>
      <p>Utilization of the latest technologies and techniques in wound care, including:</p>
      <ul>
        <li>Compression</li>
        <li>Biologic Skin Substitutes</li>
        <li>Negative Pressure Wound Therapy</li>
        <li>Collagen and Advanced Dressings</li>
        <li>Surgical/ Trauma Wounds</li>
        <li>Venous/ Arterial Wounds</li>
        <li>Debridements</li>
      </ul>
    </div>
  </article>

  <article class="panel panel--charcoal">
    <h2 class="heading">Partner with<br>Cedarbrook Wounds</h2>
    <div class="rule"></div>
    <div class="partner-list">
      <div class="partner-item"><span class="partner-item__icon"></span><div><h4>Enhanced Patient Outcomes</h4><p>Our specialized expertise in advanced wound care leads to faster healing times and improved patient satisfaction.</p></div></div>
      <div class="partner-item"><span class="partner-item__icon"></span><div><h4>Extended Reach</h4><p>Our in-home services allow your patients to receive high-quality care without the need for frequent visits, reducing the burden on your resources.</p></div></div>
      <div class="partner-item"><span class="partner-item__icon"></span><div><h4>Professional Integrity</h4><p>As a trusted partner, we uphold the highest standards of care and professionalism, reflecting positively on your clinic's reputation.</p></div></div>
      <div class="partner-item"><span class="partner-item__icon"></span><div><h4>Seamless Collaboration</h4><p>We maintain open communication with referring clinics, ensuring a coordinated approach to patient care.</p></div></div>
    </div>
  </article>

  <div class="care-photos">
    <div class="photo-1" role="img" aria-label="Hands applying a bandage wrap to a patient's arm"></div>
    <div class="photo-2" role="img" aria-label="Clinician in blue scrubs and gloves treating a patient's wrist"></div>
    <div class="photo-3" role="img" aria-label="Close-up of a bandaged hand being cared for"></div>
  </div>
</section>

</body>
</html>
```